Redesign of agriculture and industrial webshop.

We are a chemical company that develops and produces all kinds of liquids. Cleaning products but also agriculture health products are our specialty. For both of them we have seperate webshops. www.kelbrantchemics.com/agriculture and www.kelbrantchemics.com/industrials. Both working with wordpress and visual composer to create the content. We'd like a modern and new professional redesign of the webshop to optimize sales and generating new clients. We have just redesigned our main page www.kelbrantchemics.com, this is not a webshop so it has different functions. But we'd like to take the choice of color to match the webshop colors. If you need any source documents, please let me know.

Target Market(s)

Agriculture market in the Netherlands and Industrials cleaning, lubrication market in The Netherlands

Industry/Entity Type

Agriculture

Number of Pages Required

2 page

Requirements
Must have
• Marketing strategies, colors, market segment, webshop look, webshop optimization for sales.
• Please design a homepages, product page, contact page and about us page for both webshops.

```html
<!DOCTYPE html>
<html lang="en">
<head>
<meta charset="utf-8">
<title>Kelbrant – About Us</title>
<link rel="stylesheet" href="https://fonts.googleapis.com/css2?family=Ubuntu:wght@400;500;700&family=Open+Sans:wght@400;600;700&family=Roboto:wght@400;500;700&display=swap">
<style>
:root{
  --orange:#f26a10;
  --orange-dark:#e0560a;
  --green:#538a1c;
  --green-dark:#3f6d14;
  --green-light:#7bb23a;
  --ink:#1e1e1e;
  --text:#555;
  --muted:#8a8a8a;
  --topbar:#f2f2f2;
  --line:#cfcfcf;
  --white:#fff;
}
*{box-sizing:border-box;margin:0;padding:0}
html,body{width:1200px;height:3158px;overflow:hidden;background:var(--white)}
body{position:relative;font-family:"Open Sans",Arial,sans-serif;color:var(--text)}
.abs{position:absolute}
/* top bar */
.topbar{left:0;top:0;width:1200px;height:38px;background:var(--topbar);font-family:"Roboto",Arial,sans-serif;font-size:12px;color:#333}
.lang{left:178px;top:0;width:84px;height:38px;background:#e2e2e2;display:flex;align-items:center;justify-content:center;gap:6px}
.flag{width:18px;height:11px;background:linear-gradient(#2a3f8f,#2a3f8f);border:1px solid #c33}
.call{left:318px;top:12px;display:flex;gap:6px;align-items:center}
.call b{font-weight:400;color:var(--green)}
.account{right:184px;top:12px;display:flex;gap:8px}
/* header */
.logo{left:182px;top:62px;font-family:"Ubuntu",sans-serif;font-weight:700;font-size:44px;color:var(--orange);letter-spacing:-1px;line-height:1}
.search{left:447px;top:78px;width:326px;height:32px;border:1px solid #999;background:#fff;display:flex;align-items:center;gap:8px;padding-left:14px;font-size:12px;color:#777}
.cart{left:896px;top:80px;display:flex;align-items:center;gap:10px;font-family:"Roboto",sans-serif;font-size:15px;color:#333}
/* nav */
.nav{left:0;top:143px;width:1200px;height:45px;background:var(--green-light);display:flex;padding-left:190px;font-family:"Roboto",sans-serif;font-weight:500;font-size:13px;color:#fff;text-transform:uppercase}
.nav span{display:flex;align-items:center;padding:0 19px}
.nav .active{background:var(--orange)}
/* hero */
.hero{left:0;top:188px;width:1200px;height:420px;background:linear-gradient(180deg,#c9a26a 0%,#8f8a5a 22%,#4f6e2c 45%,#2f4a17 100%)}
.hero-title{left:0;top:320px;width:1200px;text-align:center;font-family:"Ubuntu",sans-serif;font-weight:500;font-size:50px;color:#fff}
.edge{left:0;width:1200px}
/* sections */
.h2{left:0;width:1200px;text-align:center;font-family:"Ubuntu",sans-serif;font-size:32px;color:var(--ink);letter-spacing:1px}
.who{left:200px;top:715px;width:800px;text-align:center;font-size:15px;line-height:25px;color:var(--text)}
.who p+p{margin-top:14px}
.values{left:0;top:1025px;width:1200px;height:435px;background:var(--green)}
.oval{width:214px;height:266px;border-radius:50%;background:var(--green-dark);top:1099px;display:flex;flex-direction:column;align-items:center;padding-top:34px;text-align:center;color:#fff}
.oval h3{font-family:"Roboto",sans-serif;font-weight:500;font-size:16px;margin-top:16px;text-transform:uppercase}
.oval p{font-size:11px;line-height:15px;color:#b9d49a;width:130px;margin-top:8px;height:48px}
.oval .down{margin-top:14px}
.stat{font-family:"Ubuntu",sans-serif}
.stat .num{font-size:34px;color:var(--orange)}
.stat .lbl{font-size:20px;color:var(--green);letter-spacing:1px;margin-top:2px}
.vline{width:1px;background:var(--line)}
.hline{height:1px;background:var(--line)}
.lake{left:0;top:1980px;width:1200px;height:503px;background:linear-gradient(180deg,#eef0ea 0%,#e3e8d8 40%,#cfdbb9 100%)}
.history{left:258px;top:2110px;width:672px;height:255px;border-radius:130px;background:#fff;text-align:center;padding:32px 80px 0}
.history h3{font-family:"Ubuntu",sans-serif;font-size:22px;color:var(--orange);font-weight:500}
.history p{font-size:14px;line-height:24px;color:#444;margin-top:14px}
.brand{display:flex;align-items:center;gap:12px;font-family:"Ubuntu",sans-serif;font-weight:700}
/* footer */
.footer{left:0;top:2843px;width:1200px;height:257px;background:var(--orange);color:#fff}
.footer h4{font-family:"Roboto",sans-serif;font-weight:700;font-size:14px;text-transform:uppercase}
.fcol{top:2898px;font-size:13px}
.fcol ul{list-style:none;margin-top:14px;line-height:25px;color:#ffe2cc}
.email{width:224px;height:34px;border:1px solid #ffd0b0;font-size:12px;padding:9px 12px;color:#ffe2cc;margin-top:12px}
.subscribe{width:118px;height:32px;background:var(--green);font-family:"Roboto",sans-serif;font-weight:700;font-size:12px;display:flex;align-items:center;justify-content:center;margin-top:14px}
.social{display:flex;gap:8px;margin-top:12px}
.social span{width:28px;height:28px;border:1.5px solid #fff;border-radius:50%}
.cards{display:flex;gap:6px;margin-top:12px}
.cards span{width:30px;height:18px;background:#fff;border-radius:2px}
.copy{left:0;top:3100px;width:1200px;height:58px;background:var(--orange-dark);color:#ffe2cc;font-size:12px;text-align:center;line-height:58px}
</style>
</head>
<body>

<div class="abs topbar">
  <div class="abs lang"><span class="flag"></span>ENG
    <svg width="10" height="6" viewBox="0 0 10 6"><path d="M1 1l4 4 4-4" stroke="#333" fill="none"/></svg></div>
  <div class="abs call">
    <svg width="13" height="13" viewBox="0 0 24 24"><path d="M6.6 10.8a15 15 0 006.6 6.6l2.2-2.2a1 1 0 011-.25 11.4 11.4 0 003.6.57 1 1 0 011 1V20a1 1 0 01-1 1A17 17 0 013 4a1 1 0 011-1h3.5a1 1 0 011 1c0 1.25.2 2.45.57 3.57a1 1 0 01-.25 1z" fill="#333"/></svg>
    CALL US <b>+31 400 12 34 56</b></div>
  <div class="abs account"><span>My Account</span>|<span>Wishlist</span>|<span>Login</span>|<span>Checkout</span></div>
</div>

<div class="abs logo">KELBRANT</div>
<div class="abs search">
  <svg width="14" height="14" viewBox="0 0 24 24"><circle cx="10" cy="10" r="7" stroke="#666" stroke-width="2.5" fill="none"/><path d="M15 15l6 6" stroke="#666" stroke-width="2.5"/></svg>
  Search here...</div>
<div class="abs cart">
  <svg width="32" height="28" viewBox="0 0 32 28"><path d="M2 9h28l-3 17H5z" fill="var(--orange)"/><path d="M9 9l5-7M23 9l-5-7" stroke="var(--orange)" stroke-width="2.5"/><path d="M8 14h16M8 19h16" stroke="#fff" stroke-width="1.5"/></svg>
  0 ITEMS</div>

<nav class="abs nav">
  <span>Home</span><span class="active">About us</span><span>Cattle</span><span>Poultry</span><span>Crop</span><span>Auxiliary products</span><span>Knowledge</span><span>Packaging</span>
</nav>

<div class="abs hero" role="img" aria-label="Photograph of a red tractor working rows of green crops in a field at sunset"></div>
<div class="abs hero-title">ABOUT US</div>
<svg class="abs edge" style="top:500px" width="1200" height="110" viewBox="0 0 1200 110" preserveAspectRatio="none">
  <path d="M0 110V88l40 4 30-10 40 8 50-14 60 6 40-12 50-8 40-6 30-22 20 6 20-22 25 8 30 10 40 16 40 6 50-6 40 10 40-4 50 8 40 12 60-2 50 10 40-6 60 8 50 6 40-4 50 10 40-2 50 8V110z" fill="#fff"/>
</svg>

<div class="abs h2" style="top:652px">WHO WE ARE</div>
<div class="abs who">
  <p>Kelbrant has been focusing on the most diverse sectors for more than 4 decades. Both in the Netherlands home market and in many countries around the world. Customers appreciate the effectiveness and high quality of the innovative products and related information, possibilities and advice from our specialists.</p>
  <p>Our B2B product lines consist mainly of liquid products that promote the comfort of the customer in different areas, both in Agriculture and Industrials. Kelbrant Chemics BV contributes in this way to offering company-specific solutions for customers. We strive for the highest possible quality, innovation and sustainability in our products, so that you can get the most out of your company.</p>
</div>

<div class="abs values"></div>
<div class="abs oval" style="left:150px">
  <svg width="60" height="60" viewBox="0 0 60 60"><circle cx="30" cy="30" r="27" stroke="#fff" stroke-width="2.5" fill="none"/><path d="M18 31l8 8 17-18" stroke="#fff" stroke-width="3" fill="none"/></svg>
  <h3>Quality</h3><p>Quality in our products, solutions and service.</p>
  <svg class="down" width="34" height="34" viewBox="0 0 34 34"><circle cx="17" cy="17" r="15" stroke="#fff" stroke-width="1.5" fill="none"/><path d="M11 14l6 6 6-6" stroke="#fff" stroke-width="2" fill="none"/></svg>
</div>
<div class="abs oval" style="left:373px">
  <svg width="60" height="60" viewBox="0 0 60 60" stroke="#fff" stroke-width="2.5" fill="none"><path d="M30 58V8"/><path d="M30 20c-6-2-9-7-9-12 6 2 9 7 9 12zM30 20c6-2 9-7 9-12-6 2-9 7-9 12zM30 34c-6-2-9-7-9-12 6 2 9 7 9 12zM30 34c6-2 9-7 9-12-6 2-9 7-9 12zM30 48c-6-2-9-7-9-12 6 2 9 7 9 12zM30 48c6-2 9-7 9-12-6 2-9 7-9 12z"/></svg>
  <h3>Agriculture</h3><p>Total solutions for the professional agricultural market.</p>
  <svg class="down" width="34" height="34" viewBox="0 0 34 34"><circle cx="17" cy="17" r="15" stroke="#fff" stroke-width="1.5" fill="none"/><path d="M11 14l6 6 6-6" stroke="#fff" stroke-width="2" fill="none"/></svg>
</div>
<div class="abs oval" style="left:594px">
  <svg width="60" height="60" viewBox="0 0 60 60" stroke="#fff" stroke-width="2.2" fill="none"><rect x="6" y="22" width="16" height="34"/><rect x="22" y="8" width="16" height="48"/><rect x="38" y="28" width="16" height="28"/><path d="M10 28h8M10 36h8M10 44h8M26 14h8M26 22h8M26 30h8M26 38h8M42 34h8M42 42h8"/></svg>
  <h3>Industrials</h3><p>Cost and labor-saving maintenance solutions.</p>
  <svg class="down" width="34" height="34" viewBox="0 0 34 34"><circle cx="17" cy="17" r="15" stroke="#fff" stroke-width="1.5" fill="none"/><path d="M11 14l6 6 6-6" stroke="#fff" stroke-width="2" fill="none"/></svg>
</div>
<div class="abs oval" style="left:813px">
  <svg width="76" height="60" viewBox="0 0 76 60" stroke="#fff" stroke-width="2.2" fill="none"><rect x="4" y="6" width="68" height="38" rx="4"/><path d="M20 44l-6 12 16-12"/><circle cx="38" cy="25" r="8"/><path d="M38 11v5M38 34v5M24 25h5M47 25h5"/></svg>
  <h3>Services</h3><p>7/7 accessible via chat for your questions.</p>
  <svg class="down" width="34" height="34" viewBox="0 0 34 34"><circle cx="17" cy="17" r="15" stroke="#fff" stroke-width="1.5" fill="none"/><path d="M11 14l6 6 6-6" stroke="#fff" stroke-width="2" fill="none"/></svg>
</div>
<svg class="abs edge" style="top:1390px" width="1200" height="72" viewBox="0 0 1200 72" preserveAspectRatio="none">
  <path d="M120 72V44l20-10 30 6 40-8 40 4 30-10 50 6 40-4 30 2 40-10 40 4 50-6 30-10 40 2 30-12 20 8 30 12 40 4 40 6 50-8 40 4 50 6 40 2 30-8 40 10V72z" fill="#fff"/>
  <rect x="0" y="66" width="1200" height="6" fill="#fff"/>
</svg>

<div class="abs h2" style="top:1522px">ABOUT US</div>
<div class="abs vline" style="left:452px;top:1610px;height:265px"></div>
<div class="abs vline" style="left:802px;top:1610px;height:265px"></div>
<div class="abs hline" style="left:203px;top:1738px;width:814px"></div>
<div class="abs stat" style="left:211px;top:1620px"><div class="num">100%</div><div class="lbl">PERSONAL ADVICE</div></div>
<div class="abs stat" style="left:516px;top:1620px"><div class="num">100%</div><div class="lbl">ENVIRONMENT</div></div>
<div class="abs stat" style="left:866px;top:1620px"><div class="num">100%</div><div class="lbl">INNOVATION</div></div>
<div class="abs stat" style="left:211px;top:1767px"><div class="num">100%</div><div class="lbl">QUALITY</div></div>
<div class="abs stat" style="left:516px;top:1767px"><div class="num">100%</div><div class="lbl">7/7 CUSTOMER SERVICE</div></div>
<div class="abs stat" style="left:866px;top:1767px"><div class="num">100%</div><div class="lbl">SAVE COSTS</div></div>

<div class="abs lake" role="img" aria-label="Faded photograph of a tractor in green crop fields"></div>
<div class="abs h2" style="top:2043px;font-size:30px">LAKE</div>
<div class="abs history">
  <h3>HISTORY</h3>
  <p>Integer congue augue et malesuada iaculis ipsum dui aliquet felis at cursus magna nisl nec elit Praesent elementum elit at tellus nec ultricies sit amet porttitor mattis enim In massa libero interdum nec interdum vel blandit sed nulla In ullamcorper est eget tempor cursus neque mi consectetuer</p>
</div>
<svg class="abs edge" style="top:2413px" width="1200" height="72" viewBox="0 0 1200 72" preserveAspectRatio="none">
  <path d="M0 72V50l40-4 40 6 50-10 40 8 60-6 50-16 30 10 40-4 30 8 60-12 40 4 50-8 40 6 50-10 40 6 60 4 40-10 50 8 40-6 50 10 40-4 60 6 40 2 50-6 50 4V72z" fill="#fff"/>
</svg>

<div class="abs h2" style="top:2540px;font-size:30px">OTHER BRANDS</div>
<div class="abs brand" style="left:205px;top:2660px;font-size:34px;color:var(--ink)"><span style="width:34px;height:34px;background:var(--ink);border-radius:50%"></span>ORVELA</div>
<div class="abs brand" style="left:488px;top:2670px;font-size:20px;color:#1e3a7a"><span style="width:26px;height:26px;background:#1e3a7a"></span>MARCEL DURAND NANOTECH</div>
<div class="abs brand" style="left:808px;top:2660px;font-size:30px;color:var(--orange)">KELBRANT</div>
<div class="abs" style="left:846px;top:2702px;font-family:'Ubuntu',sans-serif;font-size:15px;color:var(--ink)">Home Garden</div>

<footer class="abs footer"></footer>
<div class="abs fcol" style="left:186px">
  <h4>Sign up newsletter</h4>
  <div style="margin-top:14px;color:#ffe2cc">Please sign up for newsletter</div>
  <div class="email">Email address</div>
  <div class="subscribe">SUBSCRIBE</div>
</div>
<div class="abs fcol" style="left:472px"><h4>Company</h4><ul><li>Home</li><li>About Us</li><li>Our Products</li><li>Cattle</li></ul></div>
<div class="abs fcol" style="left:594px"><h4>Products</h4><ul><li>Poultry</li><li>Crop</li><li>Auxiliary Products</li><li>Knowledge</li></ul></div>
<div class="abs fcol" style="left:740px"><h4>Resources</h4><ul><li>My Account</li><li>Cart</li><li>Support</li><li>Contact Us</li></ul></div>
<div class="abs fcol" style="left:864px">
  <h4>Follow us</h4>
  <div class="social"><span></span><span></span><span></span><span></span></div>
  <div class="cards"><span></span><span></span><span></span><span></span><span></span></div>
</div>
<div class="abs copy">© 2018 Company Name  All right reserved</div>

</body>
</html>
```